Florabelle Packaging Design Project Hair Removal products

Florabelle is launching a New Hair Removal Sub Brand, under the Florabelle Brand .

This new hair removal range will include approx six products that are all designed to remove hair. These include hot wax, wax strips, depilitaory creams, hair removal lotion etc.

We are looking for a fresh new look and a sub brand name for the range. Currently we have a name Florabelle Sorbet Swish as a name option but we are not sold on this name so we would like to see other options . We would like the brand to use the same primary colours as our current florabelle brand. ie the pink and the blue but it should look different from the current range. I will email through all the pantones and logos on the brand. You can check out florabelle-example.co.za to see the current range

For the design we would like to see a design for a sticker that goes on a bottle as well as see how it translates on a box.

Target Market(s)

any female using hair removal products

Industry/Entity Type

Hair

Requirements
Must have
• simple design.

must use our colours

it must somehow portray that using our hair removal system is really quick, easy and effective

You can use images of legs on the packaging but it is not required.

all design must have the main brand logo "Florabelle" on the packaging but with regard to the sub name for the brand we are not sold on our name so we require that for one of your artwork options that you use our name "Sorbet Swish" for one of the designs , however we would also like you to come up with your own name for the hair removal range.

Florabelle logo is not dominant and can remain in the background.

```html
<!DOCTYPE html>
<html lang="en">
<head>
<meta charset="utf-8">
<title>Florabelle Sorbet Swish – Hair Removal Cream Packaging</title>
<link href="https://fonts.googleapis.com/css2?family=Raleway:wght@300;400&family=Open+Sans:wght@400&display=swap" rel="stylesheet">
<style>
  :root {
    --pink: #e0177a;
    --pink-soft: #f3a6c7;
    --blue: #2f9fd6;
    --blue-soft: #bfe2f3;
    --ink: #4a4a4a;
    --ink-light: #7a7a7a;
    --pack: #ffffff;
    --edge: #e2e2e2;
    --bg: #ffffff;
    --skin: #f2c2a6;
  }
  * { box-sizing: border-box; margin: 0; padding: 0; }
  html, body { width: 1076px; height: 1200px; overflow: hidden; background: var(--bg); }
  .stage { position: relative; width: 1076px; height: 1200px; }

  .brand { font-family: "Raleway", sans-serif; font-weight: 300; color: var(--ink); letter-spacing: 0.5px; }
  .range-name { font-family: "Raleway", sans-serif; font-weight: 400; line-height: 0.95; letter-spacing: 2px; }
  .range-type { font-family: "Raleway", sans-serif; font-weight: 400; letter-spacing: 1.5px; font-size: 11px; }
  .volume { font-family: "Open Sans", sans-serif; color: var(--ink-light); }

  /* Box */
  .box {
    position: absolute; left: 87px; top: 53px; width: 420px; height: 1000px;
    background: linear-gradient(90deg, #f7f7f7 0%, var(--pack) 12%, var(--pack) 100%);
    border: 1px solid var(--edge);
    overflow: hidden;
  }
  .box .brand { position: absolute; left: 50px; top: 140px; font-size: 40px; white-space: nowrap; }
  .box .range-name { position: absolute; left: 118px; top: 200px; font-size: 50px; color: var(--pink); }
  .box .range-type { position: absolute; left: 120px; top: 305px; font-size: 15px; color: var(--pink-soft); white-space: nowrap; }
  .box .art { position: absolute; left: 30px; top: 410px; width: 300px; height: 320px; }
  .box .band {
    position: absolute; left: 6px; top: 840px; width: 430px; height: 54px;
    background: var(--pink); color: #fff;
    font-family: "Open Sans", sans-serif; font-size: 24px; line-height: 54px; padding-left: 40px; white-space: nowrap;
  }
  .box .volume { position: absolute; left: 90px; top: 945px; font-size: 22px; white-space: nowrap; }

  /* Tubes */
  .tube { position: absolute; top: 157px; width: 352px; height: 925px; filter: drop-shadow(0 0 1px #cfcfcf); }
  .tube--blue { left: 305px; }
  .tube--pink { left: 693px; }
  .tube .body {
    position: absolute; left: 0; top: 0; width: 100%; height: 850px;
    background: var(--pack);
    clip-path: polygon(0 0, 100% 0, 97% 62%, 86% 100%, 14% 100%, 3% 62%);
  }
  .tube .crimp { position: absolute; left: 0; top: 0; width: 100%; height: 12px; background: #f1f1f1; }
  .tube .cap {
    position: absolute; left: 55px; top: 850px; width: 242px; height: 75px;
    background: linear-gradient(90deg, #efefef, var(--pack) 30%, var(--pack) 70%, #efefef);
    border-radius: 0 0 4px 4px;
  }
  .tube .label { position: absolute; left: 0; top: 0; width: 100%; text-align: center; }
  .tube .brand { position: absolute; left: 0; width: 100%; top: 118px; font-size: 30px; }
  .tube .range-name { position: absolute; left: 75px; top: 230px; font-size: 36px; text-align: left; }
  .tube .range-type { position: absolute; left: 77px; top: 294px; text-align: left; white-space: nowrap; }
  .tube .art { position: absolute; left: 20px; top: 320px; width: 270px; height: 250px; }
  .tube .tagline {
    position: absolute; left: 82px; top: 622px; width: 190px; height: 30px; border-radius: 15px;
    color: #fff; font-family: "Open Sans", sans-serif; font-size: 14px; line-height: 30px; white-space: nowrap;
  }
  .tube .volume { position: absolute; left: 0; width: 100%; top: 678px; font-size: 12px; }

  .tube--blue .range-name { color: var(--blue); }
  .tube--blue .range-type { color: var(--blue-soft); }
  .tube--blue .tagline { background: var(--blue); }
  .tube--pink .range-name { color: var(--pink); }
  .tube--pink .range-type { color: var(--pink-soft); }
  .tube--pink .tagline { background: var(--pink); }

  .legs { position: absolute; inset: 0; border-radius: 50%; }
  .legs--pink { background: radial-gradient(ellipse at 65% 45%, #f6c9d4 0%, #fbe3ea 45%, rgba(255,255,255,0) 72%); }
  .legs--blue { background: radial-gradient(ellipse at 65% 55%, #cde8f6 0%, #f7dccd 40%, rgba(255,255,255,0) 72%); }
  .swoosh { position: absolute; left: 0; top: 0; width: 100%; height: 100%; }
</style>
</head>
<body>
<main class="stage">

  <section class="box">
    <div class="brand">Florabelle</div>
    <div class="range-name">SORBET<br>SWISH</div>
    <div class="range-type">HAIR REMOVAL CREAM</div>
    <div class="art">
      <div class="legs legs--pink" role="img" aria-label="Illustration of a woman's smooth legs with a pink floral splash"></div>
      <svg class="swoosh" viewBox="0 0 300 320" aria-hidden="true">
        <path d="M150 300 Q260 300 290 190" fill="none" stroke="#b8b8b8" stroke-width="6" stroke-linecap="round"/>
      </svg>
    </div>
    <div class="band">Quick, easy and effective</div>
    <div class="volume">150 ml / 5 Fl OZ</div>
  </section>

  <section class="tube tube--blue">
    <div class="body"><div class="crimp"></div></div>
    <div class="cap"></div>
    <div class="label">
      <div class="brand">Florabelle</div>
      <div class="range-name">SORBET<br>SWISH</div>
      <div class="range-type">HAIR REMOVAL CREAM</div>
      <div class="art">
        <div class="legs legs--blue" role="img" aria-label="Illustration of a woman's smooth legs on a soft blue glow"></div>
        <svg class="swoosh" viewBox="0 0 270 250" aria-hidden="true">
          <path d="M120 240 Q230 240 255 150" fill="none" stroke="#b8b8b8" stroke-width="5" stroke-linecap="round"/>
        </svg>
      </div>
      <div class="tagline">Quick, easy and effective</div>
      <div class="volume">150 ml / 5 Fl OZ</div>
    </div>
  </section>

  <section class="tube tube--pink">
    <div class="body"><div class="crimp"></div></div>
    <div class="cap"></div>
    <div class="label">
      <div class="brand">Florabelle</div>
      <div class="range-name">SORBET<br>SWISH</div>
      <div class="range-type">HAIR REMOVAL CREAM</div>
      <div class="art">
        <div class="legs legs--pink" role="img" aria-label="Illustration of a woman's smooth legs on a soft pink glow"></div>
        <svg class="swoosh" viewBox="0 0 270 250" aria-hidden="true">
          <path d="M120 240 Q230 240 255 150" fill="none" stroke="#b8b8b8" stroke-width="5" stroke-linecap="round"/>
        </svg>
      </div>
      <div class="tagline">Quick, easy and effective</div>
      <div class="volume">150 ml / 5 Fl OZ</div>
    </div>
  </section>

</main>
</body>
</html>
```